Health and Wellbeing online Shop

I have attached a specification, however in summary this is a new business startup selling vitamins and supplements.

We need a web design for new wellbeing website, selling high end vitamins, supplements and nootropics. Therefore I need a simple eCommerce solution .

I need the website to look very different to other websites on the market. The more creative the better. It should look fresh elegant and simple. The criteria for products being on my site is that they have great reviews and they have been scientifically tested.

You will need the option of being able to log into an account, either through pagebook, snoople, chirpnet, Pixogram or create an account with email. For accounts, users will need the facility to reset passwords, see previous orders, track current order, and maintain favourites.

It should be PC, mobile and tablet friendly.

Look and Feel

It should be an elegant, modern, professional, trendy, unisex website. It should look clean and calm. Am happy to try interesting and slightly unusual designs. I would also like to have chat functionality, either powered by volKAtalk or by Bax 61.

Websites I like are
https://www.corvan-radiance.co.uk/
https://www.plainnutrients.co.uk/
http://www.lumadermis.com/

PLEASE DO USE YOUR KNOWELDGE OF WHAT WORKS FOR WEB DESIGN. YOU’RE THE EXPERT AND NEED YOUR EXPERTISE. CARTE BLANCHE TO DESIGN AS YOU SEE FIT. Please be creative, I need my site to stand out from the crowd.

Target Market(s)
Middle aged women are our most common client, however, younger patients, both male and female, will often visit the site. In summary, I would like the site to appeal to all age brackets.

Industry/Entity Type
Business

Coding
Coded - Design and coding required

Number of Pages Required
5 pages
Updates

I would like more designs. I was expecting 75+ Designs to choose from as per the package I paid for.

Target Market(s)

Industry/Entity Type

Health And Wellness

Coding

Number of Pages Required

5+ page

Requirements
Must have
• Creative design

```html
<!DOCTYPE html>
<html lang="en">
<head>
<meta charset="utf-8">
<title>Elmvale Nutrients – Your Place to Discover Wellness</title>
<link rel="stylesheet" href="https://fonts.googleapis.com/css2?family=Poppins:ital,wght@0,400;0,500;0,600;0,700;1,400&display=swap">
<style>
:root{
  --gold:#a0722e;
  --gold-dark:#8a611f;
  --ink:#2f2f33;
  --text:#55585e;
  --muted:#9a9da3;
  --line:#e6e7ea;
  --card:#ffffff;
  --page:#ffffff;
  --soft:#f4f5f7;
  --footer:#efefef;
  --heart:#e0403a;
  --star:#f2a33a;
}
*{box-sizing:border-box;margin:0;padding:0}
html,body{width:1200px;height:3828px;overflow:hidden}
body{font-family:'Poppins',sans-serif;color:var(--text);background:var(--page);position:relative;font-size:13px}
a{color:inherit;text-decoration:none}
.abs{position:absolute}
.btn{display:inline-flex;align-items:center;justify-content:center;border-radius:20px;font-weight:600;font-size:12px}
.btn-gold{background:var(--gold);color:#fff}
.btn-line{border:1px solid #cfd1d5;color:var(--text);background:#fff}

/* header */
.site-header{left:0;top:0;width:1200px;height:80px;z-index:3}
.brand{left:190px;top:14px;display:flex;flex-direction:column;align-items:center;gap:4px}
.brand-mark{width:44px;height:44px;border:1.5px solid var(--ink);border-radius:50%}
.brand-name{font-size:10px;font-weight:500;color:var(--ink);letter-spacing:.5px}
.main-nav{left:420px;top:20px;display:flex;gap:48px;font-size:12px;color:var(--ink)}
.header-icons{left:896px;top:16px;display:flex;gap:26px}
.header-icons svg{width:18px;height:18px;stroke:var(--ink);fill:none;stroke-width:1.8}

/* hero */
.hero{left:0;top:0;width:1200px;height:610px;background:linear-gradient(180deg,#f3f4f6 0%,#eef0f2 70%,#dfe4e2 100%)}
.hero-photo{left:560px;top:0;width:640px;height:610px;background:linear-gradient(180deg,#eef0f2 0%,#e7e9eb 55%,#c9d2cc 85%,#9fb09c 100%)}
.hero-copy{left:180px;top:166px;width:380px}
.hero-copy h1{font-size:42px;line-height:1.18;font-weight:700;color:#3b3d42}
.hero-copy p{margin-top:14px;font-size:14px;line-height:1.5;color:var(--text)}
.hero-copy .btn{margin-top:26px;width:122px;height:36px}

/* features */
.features{left:180px;top:528px;width:840px;display:flex;gap:30px;z-index:2}
.feature{flex:1;height:100px;background:#fff;box-shadow:0 6px 18px rgba(0,0,0,.07);display:flex;gap:16px;padding:26px 20px}
.feature svg{width:26px;height:26px;flex:none;stroke:var(--gold);fill:none;stroke-width:1.6}
.feature h3{font-size:14px;font-weight:500;color:var(--ink)}
.feature p{font-size:10px;color:var(--muted);line-height:1.5;margin-top:4px}

/* section headings */
.section-title{left:0;width:1200px;text-align:center;font-size:28px;font-weight:600;color:var(--ink)}

/* toolbar */
.toolbar{left:180px;top:786px;width:840px;display:flex;justify-content:space-between;align-items:center;font-size:12px;color:var(--muted)}
.toolbar .select{display:inline-flex;align-items:center;gap:10px;border:1px solid var(--line);padding:4px 10px;margin-left:10px;font-size:10px}
.grid-icon{width:16px;height:16px;margin-left:16px;vertical-align:middle}

/* product cards */
.product-grid{left:180px;top:848px;width:840px;display:grid;grid-template-columns:repeat(3,260px);gap:48px 30px}
.product{position:relative;height:352px;background:var(--card);box-shadow:0 4px 16px rgba(0,0,0,.07);padding:20px 22px}
.heart{position:absolute;left:20px;top:20px;width:16px;height:16px;fill:var(--heart)}
.pack{width:96px;height:150px;margin:20px auto 0;border-radius:6px}
.rating{display:flex;align-items:center;gap:2px;margin-top:22px;font-size:10px;color:var(--muted)}
.rating svg{width:11px;height:11px;fill:var(--star)}
.rating span{margin-left:8px}
.product h4{margin-top:8px;font-size:13px;font-weight:500;color:var(--ink);line-height:1.4;height:36px}
.product .foot{display:flex;justify-content:space-between;align-items:center;margin-top:16px}
.price{font-size:15px;font-weight:500;color:var(--ink)}
.product .btn{width:76px;height:28px;font-size:10px;font-weight:500;border-radius:14px}

.tone-bottle{background:linear-gradient(180deg,#e8ecef,#c8d3da);width:60px}
.tone-jar{background:linear-gradient(180deg,#6b3d22,#3c1f10);width:90px;height:130px;margin-top:36px}
.tone-tube{background:linear-gradient(180deg,#f4f5f6,#dfe3e6);width:56px}
.tone-pouch-y{background:linear-gradient(180deg,#efe9dc,#d8c486)}
.tone-pouch-g{background:linear-gradient(180deg,#eef1ee,#3f8a58)}

.view-more{left:540px;width:120px;height:38px}

/* solution band */
.solution{left:0;top:1784px;width:1200px;height:476px;background:linear-gradient(90deg,#f3f4f5 0%,#eceef0 100%)}
.solution-photo{left:560px;top:1784px;width:640px;height:476px;background:linear-gradient(135deg,#e9ebee 0%,#d9d7d4 45%,#cfc4b8 70%,#e4e6e8 100%)}
.solution-copy{left:180px;top:1876px;width:380px}
.solution-copy .eyebrow{font-size:13px;font-style:italic;color:var(--text)}
.solution-copy h2{margin-top:18px;font-size:40px;line-height:1.2;font-weight:700;color:#3b3d42}
.solution-copy p{margin-top:14px;font-size:14px;line-height:1.5}
.solution-copy .btn{margin-top:26px;width:122px;height:36px}

/* deals */
.deals{left:180px;top:2400px;width:840px;display:flex;gap:30px}
.deals .product{width:260px;height:360px}
.deals .btn-gold{border:none}
.arrow{width:36px;height:36px;border-radius:50%;display:flex;align-items:center;justify-content:center}
.arrow svg{width:14px;height:14px;stroke-width:2;fill:none}
.arrow-prev{left:110px;top:2562px;background:#fff;border:1px solid var(--line)}
.arrow-prev svg{stroke:var(--ink)}
.arrow-next{left:1054px;top:2562px;background:var(--gold)}
.arrow-next svg{stroke:#fff}
.dots{left:0;top:2820px;width:1200px;display:flex;justify-content:center;gap:10px}
.dots i{width:7px;height:7px;border-radius:50%;background:#d4d6d9}
.dots i.on{background:var(--ink)}

/* articles */
.articles{left:180px;top:2980px;width:840px;display:flex;gap:30px}
.article{width:260px}
.article .thumb{height:180px}
.thumb-eye{background:linear-gradient(135deg,#f5f5f3,#d9dde2)}
.thumb-fruit{background:linear-gradient(135deg,#f1ece8,#c73c3c 80%)}
.thumb-pills{background:linear-gradient(135deg,#6d4a2e,#c8924a 55%,#e8d5a8)}
.article .meta{margin-top:16px;font-size:9px;color:var(--muted)}
.article h5{margin-top:8px;font-size:12px;font-weight:500;color:var(--ink);line-height:1.45}
.article p{margin-top:8px;font-size:10px;color:var(--muted);line-height:1.5}
.read-more{margin-top:14px;display:flex;align-items:center;gap:8px;font-size:12px;font-weight:500;color:var(--gold)}
.read-more svg{width:18px;height:10px;stroke:var(--gold);fill:none;stroke-width:1.6}

/* footer */
.site-footer{left:0;top:3488px;width:1200px;height:340px;background:var(--footer)}
.foot-brand{left:200px;top:3540px;width:200px}
.foot-brand .brand-mark{width:40px;height:40px;margin-left:24px}
.foot-brand .brand-name{display:block;margin-top:6px}
.foot-brand p{margin-top:20px;font-size:10px;line-height:1.6;color:var(--text)}
.socials{display:flex;gap:10px;margin-top:14px}
.socials i{width:10px;height:10px;border-radius:50%;background:#6b6e74}
.foot-col{top:3570px}
.foot-col h6{font-size:13px;font-weight:600;color:var(--ink)}
.foot-col ul{list-style:none;margin-top:18px}
.foot-col li{font-size:10px;line-height:2.4;color:var(--text)}
.contact li{display:flex;align-items:center;gap:10px}
.contact .dot{width:16px;height:16px;border-radius:50%;border:1px solid #b9bcc1;flex:none}
.copyright{left:0;top:3768px;width:1200px;text-align:center;font-size:9px;color:var(--muted)}
.foot-rule{left:200px;top:3746px;width:800px;height:1px;background:#dfe0e2}
</style>
</head>
<body>

<section class="hero abs"></section>
<div class="hero-photo abs" role="img" aria-label="Smiling man and woman in black sportswear jogging together beside a lake"></div>

<header class="site-header abs">
  <a class="brand abs" href="#"><span class="brand-mark"></span><span class="brand-name">Elmvale Nutrients</span></a>
  <nav class="main-nav abs"><a href="#">Home</a><a href="#">Vitamins</a><a href="#">Nootropics</a><a href="#">Contact</a><a href="#">About Us</a></nav>
  <div class="header-icons abs">
    <svg viewBox="0 0 24 24"><circle cx="10.5" cy="10.5" r="6.5"/><path d="M15.5 15.5L21 21"/></svg>
    <svg viewBox="0 0 24 24"><circle cx="12" cy="8" r="4"/><path d="M4 21c1.5-4 4.5-6 8-6s6.5 2 8 6"/></svg>
    <svg viewBox="0 0 24 24"><path d="M5 8h14l-1 13H6z"/><path d="M9 8V6a3 3 0 016 0v2"/></svg>
  </div>
</header>

<div class="hero-copy abs">
  <h1>Your Place to Discover Wellness.</h1>
  <p>Lorem ipsum dolor sit amet consectetur adipiscing elit tempor incididunt.</p>
  <a class="btn btn-gold" href="#">Shop Now</a>
</div>

<div class="features abs">
  <div class="feature">
    <svg viewBox="0 0 24 24"><path d="M2 6h12v10H2zM14 10h4l3 3v3h-7z"/><circle cx="6" cy="17.5" r="1.8"/><circle cx="17" cy="17.5" r="1.8"/></svg>
    <div><h3>Free Shipping</h3><p>Free delivery on every order over twenty pounds</p></div>
  </div>
  <div class="feature">
    <svg viewBox="0 0 24 24"><path d="M4 14v-2a8 8 0 0116 0v2"/><rect x="3" y="13" width="4" height="6" rx="1"/><rect x="17" y="13" width="4" height="6" rx="1"/></svg>
    <div><h3>24/7 Support</h3><p>Friendly help any time you need us most</p></div>
  </div>
  <div class="feature">
    <svg viewBox="0 0 24 24"><rect x="5" y="11" width="14" height="10" rx="1"/><path d="M8 11V7a4 4 0 018 0v4"/></svg>
    <div><h3>Secure Payment</h3><p>Safe checkout with fully encrypted card payments</p></div>
  </div>
</div>

<h2 class="section-title abs" style="top:722px">Popular Products</h2>

<div class="toolbar abs">
  <div>Sort By <span class="select">Top Sellers <svg width="8" height="6" viewBox="0 0 8 6"><path d="M1 1l3 3 3-3" stroke="#999" fill="none"/></svg></span></div>
  <div>Show <span class="select">6 <svg width="8" height="6" viewBox="0 0 8 6"><path d="M1 1l3 3 3-3" stroke="#999" fill="none"/></svg></span>
    <svg class="grid-icon" viewBox="0 0 16 16" fill="#55585e"><rect x="0" y="0" width="4" height="4"/><rect x="6" y="0" width="4" height="4"/><rect x="12" y="0" width="4" height="4"/><rect x="0" y="6" width="4" height="4"/><rect x="6" y="6" width="4" height="4"/><rect x="12" y="6" width="4" height="4"/><rect x="0" y="12" width="4" height="4"/><rect x="6" y="12" width="4" height="4"/><rect x="12" y="12" width="4" height="4"/></svg>
  </div>
</div>

<svg width="0" height="0" style="position:absolute">
  <defs>
    <path id="heart" d="M8 14.5S1.5 10.3 1.5 5.8A3.3 3.3 0 018 4.3a3.3 3.3 0 016.5 1.5C14.5 10.3 8 14.5 8 14.5z"/>
    <path id="star" d="M6 .6l1.6 3.5 3.8.4-2.9 2.6.8 3.7L6 8.9 2.7 10.8l.8-3.7L.6 4.5l3.8-.4z"/>
  </defs>
</svg>

<div class="product-grid abs">
  <article class="product">
    <svg class="heart" viewBox="0 0 16 16"><use href="#heart"/></svg>
    <div class="pack tone-bottle" role="img" aria-label="Slim pump bottle of eye cream with orange tag"></div>
    <div class="rating"><svg viewBox="0 0 12 12"><use href="#star"/></svg><svg viewBox="0 0 12 12"><use href="#star"/></svg><svg viewBox="0 0 12 12"><use href="#star"/></svg><svg viewBox="0 0 12 12"><use href="#star"/></svg><svg viewBox="0 0 12 12"><use href="#star"/></svg><span>4.9</span></div>
    <h4>Lumera Dark Circle Reduction Cream</h4>
    <div class="foot"><span class="price">£21.99</span><a class="btn btn-line" href="#">Shop Now</a></div>
  </article>
  <article class="product">
    <svg class="heart" viewBox="0 0 16 16"><use href="#heart"/></svg>
    <div class="pack tone-jar" role="img" aria-label="Amber supplement jar"></div>
    <div class="rating"><svg viewBox="0 0 12 12"><use href="#star"/></svg><svg viewBox="0 0 12 12"><use href="#star"/></svg><svg viewBox="0 0 12 12"><use href="#star"/></svg><svg viewBox="0 0 12 12"><use href="#star"/></svg><svg viewBox="0 0 12 12"><use href="#star"/></svg><span>4.9</span></div>
    <h4>Triple Strength 1000mg 95% Liquid Curcumin x 60</h4>
    <div class="foot"><span class="price">£20.15</span><a class="btn btn-line" href="#">Shop Now</a></div>
  </article>
  <article class="product">
    <svg class="heart" viewBox="0 0 16 16"><use href="#heart"/></svg>
    <div class="pack tone-tube" role="img" aria-label="White lotion bottle"></div>
    <div class="rating"><svg viewBox="0 0 12 12"><use href="#star"/></svg><svg viewBox="0 0 12 12"><use href="#star"/></svg><svg viewBox="0 0 12 12"><use href="#star"/></svg><svg viewBox="0 0 12 12"><use href="#star"/></svg><svg viewBox="0 0 12 12"><use href="#star"/></svg><span>4.9</span></div>
    <h4>Firmaline 18ml+ - The ultimate butt toning lotion</h4>
    <div class="foot"><span class="price">£23.99</span><a class="btn btn-line" href="#">Shop Now</a></div>
  </article>
  <article class="product">
    <svg class="heart" viewBox="0 0 16 16"><use href="#heart"/></svg>
    <div class="pack tone-pouch-y" role="img" aria-label="Vitamin D3 tablet pouch with yellow label"></div>
    <div class="rating"><svg viewBox="0 0 12 12"><use href="#star"/></svg><svg viewBox="0 0 12 12"><use href="#star"/></svg><svg viewBox="0 0 12 12"><use href="#star"/></svg><svg viewBox="0 0 12 12"><use href="#star"/></svg><svg viewBox="0 0 12 12"><use href="#star"/></svg><span>4.9</span></div>
    <h4>Super Strength Vitamin D3 Tablets - 4000iu</h4>
    <div class="foot"><span class="price">£6.95</span><a class="btn btn-line" href="#">Shop Now</a></div>
  </article>
  <article class="product">
    <svg class="heart" viewBox="0 0 16 16"><use href="#heart"/></svg>
    <div class="pack tone-jar" role="img" aria-label="Amber supplement jar"></div>
    <div class="rating"><svg viewBox="0 0 12 12"><use href="#star"/></svg><svg viewBox="0 0 12 12"><use href="#star"/></svg><svg viewBox="0 0 12 12"><use href="#star"/></svg><svg viewBox="0 0 12 12"><use href="#star"/></svg><svg viewBox="0 0 12 12"><use href="#star"/></svg><span>4.9</span></div>
    <h4>Triple Strength 1000mg 95% Liquid Curcumin x 60</h4>
    <div class="foot"><span class="price">£20.15</span><a class="btn btn-line" href="#">Shop Now</a></div>
  </article>
  <article class="product">
    <svg class="heart" viewBox="0 0 16 16"><use href="#heart"/></svg>
    <div class="pack tone-pouch-g" role="img" aria-label="Peppermint oil capsule pouch with green label"></div>
    <div class="rating"><svg viewBox="0 0 12 12"><use href="#star"/></svg><svg viewBox="0 0 12 12"><use href="#star"/></svg><svg viewBox="0 0 12 12"><use href="#star"/></svg><svg viewBox="0 0 12 12"><use href="#star"/></svg><svg viewBox="0 0 12 12"><use href="#star"/></svg><span>4.9</span></div>
    <h4>Peppermint Oil Capsules 50mg</h4>
    <div class="foot"><span class="price">£7.95</span><a class="btn btn-line" href="#">Shop Now</a></div>
  </article>
</div>

<a class="btn btn-gold view-more abs" style="top:1678px" href="#">View More</a>

<section class="solution abs"></section>
<div class="solution-photo abs" role="img" aria-label="Woman in sports top running with earphones and an arm band"></div>
<div class="solution-copy abs">
  <div class="eyebrow">Our solution</div>
  <h2>The Future Of Quality Your Health</h2>
  <p>Lorem ipsum dolor sit amet consectetur adipiscing elit tempor incididunt.</p>
  <a class="btn btn-gold" href="#">Get Started</a>
</div>

<h2 class="section-title abs" style="top:2310px">Today’s Top Deals</h2>

<a class="arrow arrow-prev abs" href="#"><svg viewBox="0 0 14 14"><path d="M9 2L4 7l5 5"/></svg></a>
<div class="deals abs">
  <article class="product">
    <svg class="heart" viewBox="0 0 16 16"><use href="#heart"/></svg>
    <div class="pack tone-pouch-g" role="img" aria-label="Peppermint oil capsule pouch with green label"></div>
    <div class="rating"><svg viewBox="0 0 12 12"><use href="#star"/></svg><svg viewBox="0 0 12 12"><use href="#star"/></svg><svg viewBox="0 0 12 12"><use href="#star"/></svg><svg viewBox="0 0 12 12"><use href="#star"/></svg><svg viewBox="0 0 12 12"><use href="#star"/></svg><span>4.9</span></div>
    <h4>Peppermint Oil Capsules 50mg</h4>
    <div class="foot"><span class="price">£7.95</span><a class="btn btn-gold" href="#">Shop Now</a></div>
  </article>
  <article class="product">
    <svg class="heart" viewBox="0 0 16 16"><use href="#heart"/></svg>
    <div class="pack tone-bottle" role="img" aria-label="Slim pump bottle of eye cream with orange tag"></div>
    <div class="rating"><svg viewBox="0 0 12 12"><use href="#star"/></svg><svg viewBox="0 0 12 12"><use href="#star"/></svg><svg viewBox="0 0 12 12"><use href="#star"/></svg><svg viewBox="0 0 12 12"><use href="#star"/></svg><svg viewBox="0 0 12 12"><use href="#star"/></svg><span>4.9</span></div>
    <h4>Lumera Dark Circle Reduction Cream</h4>
    <div class="foot"><span class="price">£21.99</span><a class="btn btn-gold" href="#">Shop Now</a></div>
  </article>
  <article class="product">
    <svg class="heart" viewBox="0 0 16 16"><use href="#heart"/></svg>
    <div class="pack tone-jar" role="img" aria-label="Amber supplement jar"></div>
    <div class="rating"><svg viewBox="0 0 12 12"><use href="#star"/></svg><svg viewBox="0 0 12 12"><use href="#star"/></svg><svg viewBox="0 0 12 12"><use href="#star"/></svg><svg viewBox="0 0 12 12"><use href="#star"/></svg><svg viewBox="0 0 12 12"><use href="#star"/></svg><span>4.9</span></div>
    <h4>Triple Strength 1000mg 95% Liquid Curcumin x 60</h4>
    <div class="foot"><span class="price">£20.15</span><a class="btn btn-gold" href="#">Shop Now</a></div>
  </article>
</div>
<a class="arrow arrow-next abs" href="#"><svg viewBox="0 0 14 14"><path d="M5 2l5 5-5 5"/></svg></a>
<div class="dots abs"><i></i><i class="on"></i><i></i><i></i></div>

<h2 class="section-title abs" style="top:2870px">Latest Health Articles</h2>

<div class="articles abs">
  <article class="article">
    <div class="thumb thumb-eye" role="img" aria-label="Eye test chart with a pair of glasses"></div>
    <div class="meta">Mar - 2019 &nbsp;·&nbsp; 3 Comments</div>
    <h5>3 million British adults haven’t had an eye test in more than 5 years</h5>
    <p>Regular checks help spot problems early and keep your sight sharp.</p>
    <a class="read-more" href="#">Read More <svg viewBox="0 0 18 10"><path d="M0 5h16M12 1l4 4-4 4"/></svg></a>
  </article>
  <article class="article">
    <div class="thumb thumb-fruit" role="img" aria-label="Bowl of red berries and fresh fruit on a table"></div>
    <div class="meta">Mar - 2019 &nbsp;·&nbsp; 5 Comments</div>
    <h5>Autumn is the time to build a stronger immune system</h5>
    <p>Simple seasonal habits and nutrients that support your natural defences.</p>
    <a class="read-more" href="#">Read More <svg viewBox="0 0 18 10"><path d="M0 5h16M12 1l4 4-4 4"/></svg></a>
  </article>
  <article class="article">
    <div class="thumb thumb-pills" role="img" aria-label="Hand holding a blister pack of vitamin capsules"></div>
    <div class="meta">Feb - 2019 &nbsp;·&nbsp; 2 Comments</div>
    <h5>March is when vitamin D levels are the lowest</h5>
    <p>Why winter leaves us short and how a daily dose can help.</p>
    <a class="read-more" href="#">Read More <svg viewBox="0 0 18 10"><path d="M0 5h16M12 1l4 4-4 4"/></svg></a>
  </article>
</div>

<a class="btn btn-gold view-more abs" style="top:3380px" href="#">View More</a>

<footer class="site-footer abs"></footer>
<div class="foot-brand abs">
  <span class="brand-mark" style="display:block"></span>
  <span class="brand-name">Elmvale Nutrients</span>
  <p>Quality vitamins and supplements, tested and trusted by our customers.</p>
  <div class="socials"><i></i><i></i><i></i><i></i></div>
</div>
<div class="foot-col abs" style="left:508px">
  <h6>Quick Links</h6>
  <ul><li>Vitamins</li><li>Nootropics</li><li>Contact</li><li>About Us</li></ul>
</div>
<div class="foot-col abs" style="left:664px">
  <h6>Help</h6>
  <ul><li>Contact Us</li><li>Login</li><li>Privacy policy</li></ul>
</div>
<div class="foot-col contact abs" style="left:804px">
  <h6>Contact Us</h6>
  <ul>
    <li><span class="dot"></span>Monday - Friday 9AM - 6PM</li>
    <li><span class="dot"></span>+44 (0)20 4960 1187</li>
    <li><span class="dot"></span>hello@elmvalenutrients.co.uk</li>
  </ul>
</div>
<div class="foot-rule abs"></div>
<div class="copyright abs">Copyright © 2019 All rights reserved</div>

</body>
</html>
```